Tolvane Air Center needs a new upscale business card design for our high end aircraft hangar complex

Tolvane Air Center (TAC) is a large, upscale jet hangar complex in the US housing expensive aircraft. We need a new business card design, using our current logo. We will be attending a industry convention and need a card design that will stand out and be remembered by aircraft owners and private pilots.

Target Market(s)

Aircraft pilots or owners looking for a new upscale hangar

Industry/Entity Type

Airport

I like to use very heavy card stock, 400#, double sided. Square, no rounded edges please.

Colors
3276b5
0255a3
85abd2

Requirements
Must have
• An expensive, classy design, vivid colors.
Nice to have
• Needs to look very expensive and classy, and have some "pop". Designer must be able to download or copy my current typeface or fonts.
• One card side might be black with the "Logo and Tolvane Air Center Double line image in blue (or try gold, or glossy black), and perhaps have a grayed out "R470 jet silhouette". The other card side would have our contact info, and perhaps the "TAC Logo only". I'd like my contact info 'stacked', not in a paragraph format.
Should not have
• Should not look "too busy". Having a double-sided card will help.

```html
<!DOCTYPE html>
<html lang="en">
<head>
<meta charset="UTF-8">
<title>Tolvane Air Center – Business Card</title>
<link href="https://fonts.googleapis.com/css2?family=Arimo:wght@400;700&display=swap" rel="stylesheet">
<style>
  :root {
    --page-bg: #d9d6d2;
    --card-black: #1b1b1d;
    --card-edge: #2a2a2d;
    --brand-blue: #3276b5;
    --brand-deep: #0255a3;
    --brand-light: #85abd2;
    --text-light: #e9e9ea;
    --text-muted: #b9b9bd;
    --emboss: #4a4a4e;
  }
  * { box-sizing: border-box; margin: 0; padding: 0; }
  html, body {
    width: 1200px; height: 787px; overflow: hidden;
    background: var(--page-bg);
    font-family: "Arimo", Arial, sans-serif;
  }
  .canvas {
    width: 1200px; height: 787px;
    display: flex; align-items: center; justify-content: center; gap: 40px;
  }
  .card {
    width: 540px; height: 309px;
    background: var(--card-black);
    border: 1px solid var(--card-edge);
    position: relative;
    box-shadow: 0 10px 30px rgba(0,0,0,.25);
  }
  /* Front side */
  .card-front { display: flex; flex-direction: column; align-items: center; justify-content: center; }
  .front-mark {
    font-weight: 700; font-size: 96px; letter-spacing: 4px;
    color: var(--emboss); line-height: 1;
  }
  .front-web {
    margin-top: 36px; font-size: 15px; letter-spacing: 3px; color: var(--text-muted);
  }
  /* Back side */
  .card-back { display: flex; align-items: center; padding: 0 34px 0 40px; }
  .back-brand {
    width: 210px;
    color: var(--brand-blue); font-weight: 700;
    font-size: 30px; line-height: 1.15; text-transform: uppercase;
  }
  .divider {
    width: 1px; height: 240px; margin: 0 26px 0 18px;
    background: linear-gradient(to bottom, transparent, #8c8c92 20%, #8c8c92 80%, transparent);
  }
  .contact { color: var(--text-light); font-size: 14px; line-height: 1.45; }
  .contact-name { color: var(--brand-blue); font-size: 19px; font-weight: 700; }
  .contact-title { font-size: 16px; margin-bottom: 8px; }
  .contact-address { margin-bottom: 8px; }
  .contact-line { display: flex; align-items: center; gap: 10px; }
  .contact-line svg { width: 13px; height: 13px; fill: var(--brand-blue); flex: none; }
  .contact-web { padding-left: 23px; }
</style>
</head>
<body>
<main class="canvas">
  <section class="card card-front" aria-label="Card front">
    <div class="front-mark">TAC</div>
    <div class="front-web">www.tolvaneair.com</div>
  </section>

  <section class="card card-back" aria-label="Card back">
    <div class="back-brand">Tolvane Air Center</div>
    <div class="divider"></div>
    <div class="contact">
      <div class="contact-name">Dana Whitlock</div>
      <div class="contact-title">President</div>
      <div class="contact-address">2710 Harrow Field Road<br>Cedar Bluff, NY 11720</div>
      <div class="contact-line">
        <svg viewBox="0 0 24 24" aria-hidden="true"><path d="M6.6 10.8a15.1 15.1 0 0 0 6.6 6.6l2.2-2.2a1 1 0 0 1 1-.25 11.4 11.4 0 0 0 3.6.57 1 1 0 0 1 1 1V20a1 1 0 0 1-1 1A17 17 0 0 1 3 4a1 1 0 0 1 1-1h3.5a1 1 0 0 1 1 1c0 1.25.2 2.45.57 3.57a1 1 0 0 1-.25 1z"/></svg>
        <span>631 555 0142</span>
      </div>
      <div class="contact-line">
        <svg viewBox="0 0 24 24" aria-hidden="true"><path d="M7 1h10a2 2 0 0 1 2 2v18a2 2 0 0 1-2 2H7a2 2 0 0 1-2-2V3a2 2 0 0 1 2-2zm0 3v14h10V4zm5 15.5a1 1 0 1 0 0 2 1 1 0 0 0 0-2z"/></svg>
        <span>631 555 0187</span>
      </div>
      <div class="contact-line">
        <svg viewBox="0 0 24 24" aria-hidden="true"><path d="M6 2h9l3 3v4H6zM4 10h16a2 2 0 0 1 2 2v7h-4v3H6v-3H2v-7a2 2 0 0 1 2-2zm4 7v3h8v-3z"/></svg>
        <span>631 555 0119</span>
      </div>
      <div class="contact-line">
        <svg viewBox="0 0 24 24" aria-hidden="true"><path d="M2 5h20v14H2zm2 2v.5l8 5 8-5V7zm0 2.9V17h16V9.9l-8 5z"/></svg>
        <span>dana@tolvaneair.com</span>
      </div>
      <div class="contact-web">www.tolvaneair.com</div>
    </div>
  </section>
</main>
</body>
</html>
```